Business Card Design Project

A double sided business card for presentation to business leaders in corporate.

Target Market(s)

Corporate, business professionals, HR

Industry/Entity Type

Business

Requirements
Must have
• FRONT

Logo

www.brightlanecoaching.com.au

BACK

Mara Pollen-Drew
Director

+ 61 (0) 418 536 204
mara@brightlanecoaching.com.au
www.brightlanecoaching.com.au

Impact through energy and employee engagement

("ripples" of logo, bottom corner)

Must be:
- double sided
size: 86 x 54mm
supplied as one pdf with crop marks shown (+- 1mm, with 2-3 mm bleed)

```html
<!DOCTYPE html>
<html lang="en">
<head>
<meta charset="utf-8">
<title>Brightlane Coaching – Business Card</title>
<link rel="stylesheet" href="https://fonts.googleapis.com/css2?family=Questrial&display=swap">
<style>
  :root {
    --plum: #7b2766;
    --plum-light: #9a4585;
    --plum-dark: #5e1a4e;
    --ink: #4a4a4a;
    --paper: #ffffff;
    --stage-dark: #0b0b0b;
    --stage-light: #5c5c5c;
  }
  * { margin: 0; padding: 0; box-sizing: border-box; }
  html, body { width: 1200px; height: 900px; overflow: hidden; }
  body {
    position: relative;
    background: linear-gradient(160deg, var(--stage-dark) 0%, #2a2a2a 45%, var(--stage-light) 100%);
    font-family: "Questrial", "Century Gothic", sans-serif;
  }
  .card {
    position: absolute;
    top: 245px;
    width: 572px;
    height: 358px;
    overflow: hidden;
    background: var(--paper);
    box-shadow: 3px 4px 8px rgba(0,0,0,0.55);
  }
  .card--front { left: 18px; }
  .card--back { left: 612px; width: 570px; }

  .front-art { position: absolute; inset: 0; }

  .wordmark {
    position: absolute;
    display: flex;
    align-items: center;
    gap: 12px;
    color: var(--plum);
    line-height: 0.95;
  }
  .wordmark__dot {
    flex: none;
    border-radius: 50%;
    background: var(--plum);
  }
  .wordmark__name { display: block; }
  .card--front .wordmark { left: 232px; top: 128px; font-size: 50px; }
  .card--front .wordmark__dot { width: 22px; height: 22px; }

  .front-url {
    position: absolute;
    left: 11px;
    bottom: 9px;
    color: var(--paper);
    font-size: 18px;
    letter-spacing: 0.2px;
  }

  .back-panel {
    position: absolute;
    left: 0; top: 0;
    width: 291px; height: 100%;
    background: linear-gradient(150deg, var(--plum-dark) 0%, var(--plum) 45%, var(--plum-light) 100%);
  }
  .back-strip {
    position: absolute;
    right: 2px; top: 0;
    width: 12px; height: 236px;
    background: var(--plum);
  }
  .person {
    position: absolute;
    right: 26px;
    top: 10px;
    text-align: right;
  }
  .person__name { color: var(--plum); font-size: 26px; font-weight: 400; }
  .person__role { color: var(--ink); font-size: 17px; margin-top: 2px; }

  .contact {
    position: absolute;
    right: 289px;
    bottom: 8px;
    list-style: none;
    text-align: right;
    color: var(--paper);
    font-size: 15.5px;
    line-height: 19.5px;
  }
  .card--back .wordmark { right: 20px; bottom: 14px; font-size: 30px; gap: 8px; }
  .card--back .wordmark__dot { width: 14px; height: 14px; }
</style>
</head>
<body>

<section class="card card--front" aria-label="Card front">
  <svg class="front-art" width="572" height="358" viewBox="0 0 572 358" aria-hidden="true">
    <defs>
      <linearGradient id="frontPlum" x1="0" y1="0" x2="1" y2="1">
        <stop offset="0" stop-color="#8d3c7a"/>
        <stop offset="0.55" stop-color="#7b2766"/>
        <stop offset="1" stop-color="#5e1a4e"/>
      </linearGradient>
    </defs>
    <rect width="572" height="358" fill="url(#frontPlum)"/>
    <path d="M240 0 C190 60 170 170 230 260 C260 305 290 335 312 358 L572 358 L572 0 Z" fill="#5e1a4e" opacity="0.85"/>
    <path d="M260 0 C200 70 185 170 235 255 C262 300 290 333 314 358 L572 358 L572 0 Z" fill="#ffffff"/>
  </svg>
  <div class="wordmark">
    <span class="wordmark__dot"></span>
    <span class="wordmark__name">brightlane<br>coaching</span>
  </div>
  <p class="front-url">www.brightlanecoaching.com.au</p>
</section>

<section class="card card--back" aria-label="Card back">
  <div class="back-panel"></div>
  <div class="back-strip"></div>
  <div class="person">
    <h1 class="person__name">Mara Pollen-Drew</h1>
    <p class="person__role">Director</p>
  </div>
  <ul class="contact">
    <li>+ 61 (0) 418 536 204</li>
    <li>mara@brightlanecoaching.com.au</li>
    <li>www.brightlanecoaching.com.au</li>
  </ul>
  <div class="wordmark">
    <span class="wordmark__dot"></span>
    <span class="wordmark__name">brightlane<br>coaching</span>
  </div>
</section>

</body>
</html>
```